Vela Stewardship Business Card design

We need a creative business card design for our hospitality management company
We need the following information:
Our business Logo: Vela Stewardship
Name: Mara Dobrinsky
Phone number: 0458 317 642
Email: mara@velastewardship.com.au
Address: 214/53 Penrose Street, North Elmswood 3187
Web: www.velastewardship.com.au
I need the design to be a working file so that I can insert the names and numbers of the other staff members of our business.
The cards need to be 90 x 40mm
Thanks
Industry/Entity Type
Hospitality
Look and feel

```html
<!DOCTYPE html>
<html lang="en">
<head>
<meta charset="utf-8">
<title>Vela Stewardship – Business Card</title>
<link rel="stylesheet" href="https://fonts.googleapis.com/css2?family=Open+Sans:wght@600;700&display=swap">
<style>
  :root {
    --bg-centre: #424242;
    --bg-edge: #161616;
    --wave-blue: #3ba4e8;
    --wave-edge: #e8eef2;
    --brand-text: #d9d9d9;
    --brand-square: #3ba4e8;
    --name-text: #c9c9c9;
    --label-text: #8c8c8c;
    --value-text: #dcdcdc;
  }
  html, body {
    margin: 0;
    padding: 0;
    overflow: hidden;
    background: #ffffff;
  }
  .card {
    position: relative;
    width: 1200px;
    height: 532px;
    overflow: hidden;
    background: radial-gradient(ellipse 760px 520px at 400px 270px, var(--bg-centre) 0%, #2c2c2c 50%, var(--bg-edge) 100%);
    font-family: "Open Sans", Arial, sans-serif;
    font-weight: 600;
  }
  .card__wave {
    position: absolute;
    inset: 0;
  }
  .brand {
    position: absolute;
    left: 26px;
    top: 26px;
    display: flex;
    align-items: center;
    gap: 22px;
  }
  .brand__square {
    width: 112px;
    height: 110px;
    background: var(--brand-square);
  }
  .brand__name {
    color: var(--brand-text);
    font-size: 36px;
    font-weight: 700;
    letter-spacing: 0.5px;
    text-transform: uppercase;
    margin-top: -6px;
  }
  .staff {
    position: absolute;
    left: 701px;
    top: 98px;
    margin: 0;
    padding: 0;
    list-style: none;
    color: var(--name-text);
  }
  .staff__name {
    font-size: 37px;
    line-height: 44px;
    letter-spacing: 0.8px;
  }
  .staff__other {
    font-size: 30px;
    line-height: 44px;
    letter-spacing: 0.6px;
  }
  .contact {
    position: absolute;
    left: 27px;
    top: 265px;
    margin: 0;
    font-size: 22px;
    line-height: 27px;
    letter-spacing: 0.5px;
  }
  .contact__row { margin: 0; white-space: nowrap; }
  .contact__label { color: var(--label-text); }
  .contact__value { color: var(--value-text); }
</style>
</head>
<body>
  <div class="card">
    <svg class="card__wave" width="1200" height="532" viewBox="0 0 1200 532" aria-hidden="true">
      <path d="M0,433 C120,470 260,484 420,470 C700,446 980,362 1200,268 L1200,532 L0,532 Z" fill="var(--wave-blue)"/>
      <path d="M0,433 C120,470 260,484 420,470 C700,446 980,362 1200,268" fill="none" stroke="var(--wave-edge)" stroke-width="1.5" opacity="0.7"/>
    </svg>

    <div class="brand">
      <div class="brand__square"></div>
      <span class="brand__name">Vela Stewardship</span>
    </div>

    <ul class="staff">
      <li class="staff__name">Mara Dobrinsky</li>
      <li class="staff__other">Insert other name here</li>
      <li class="staff__other">Insert other name here</li>
      <li class="staff__other">Insert other name here</li>
    </ul>

    <div class="contact">
      <p class="contact__row"><span class="contact__label">Phone number:</span> <span class="contact__value">0458 317 642</span></p>
      <p class="contact__row"><span class="contact__label">Email:</span> <span class="contact__value">mara@velastewardship.com.au</span></p>
      <p class="contact__row"><span class="contact__label">Website:</span> <span class="contact__value">www.velastewardship.com.au</span></p>
      <p class="contact__row"><span class="contact__label">Address:</span> <span class="contact__value">214/53 Penrose Street, North Elmswood 3187</span></p>
    </div>
  </div>
</body>
</html>
```